R. T. HOLLOWAY, INC. is a US based Investment firm looking for a five-page website design.

Currently, their temporary site is located at: rtholloway.com and they would like to maintain the site design as much as possible.

R. T. HOLLOWAY, INC. sister companies are: Crestvale Lodge Investments (c-lodge.com) Benwick Petroleum (benwick-petroleum.com) and RTHF (rth-foundation.org/en)

Attached is a .ZIP file with designs and assets we think will be useful for your proposal… Content for the site is attached on: rtholloway website content.docx Current temp website design is attached as: Coming Soon Website.zip .EPS Logo files attached as: rtholloway logos.zip Sample business card attached as: R T Holloway Business cards.eps Other assets, such as Fonts and background images attached as: Assets.zip

Target Market(s)

Investors

Industry/Entity Type

Investments

Number of Pages Required

5+ page

Requirements
Must have
• Contact Page with a form.

```html
<!DOCTYPE html>
<html lang="en">
<head>
<meta charset="utf-8">
<title>R. T. Holloway, Inc.</title>
<link rel="stylesheet" href="https://fonts.googleapis.com/css2?family=Mulish:wght@400;600;700;800&family=Tinos:wght@400;700&display=swap">
<style>
  :root {
    --gold: #b59d5c;
    --navy: #253240;
    --ink: #252f3b;
    --text: #3a3f47;
    --white: #ffffff;
    --soft-shadow: rgba(30, 40, 55, 0.10);
  }
  * { margin: 0; padding: 0; box-sizing: border-box; }
  html, body { width: 888px; height: 1200px; overflow: hidden; background: var(--white); }
  body { position: relative; font-family: "Mulish", sans-serif; color: var(--text); }
  .abs { position: absolute; }

  .hero-art { position: absolute; left: 0; top: 0; width: 888px; height: 440px; }

  .brand { left: 104px; top: 9px; width: 118px; text-align: center; color: var(--white); }
  .brand-ring { width: 30px; height: 30px; border: 2px solid var(--gold); border-radius: 50%; margin: 0 auto 4px; }
  .brand-name { font-family: "Tinos", serif; font-size: 14px; line-height: 16px; letter-spacing: 0.3px; }

  .nav { top: 40px; left: 364px; display: flex; gap: 17px; font-family: "Tinos", serif; font-size: 12.5px; color: var(--white); }
  .nav-cta { left: 704px; top: 37px; width: 79px; height: 25px; border: 1px solid var(--gold); border-radius: 13px;
             color: var(--gold); font-size: 10px; line-height: 23px; text-align: center; }

  .hero-text { left: 0; width: 888px; text-align: center; color: var(--white); }
  .hero-kicker { top: 174px; font-family: "Tinos", serif; font-weight: 700; font-size: 16px; }
  .hero-title { top: 198px; font-weight: 800; font-size: 19px; line-height: 27px; }
  .hero-btn { left: 379px; top: 266px; width: 130px; height: 29px; border-radius: 15px; background: var(--gold);
              color: var(--white); font-size: 10.5px; line-height: 29px; text-align: center; }

  .section-title { top: 484px; left: 0; width: 888px; text-align: center; font-family: "Tinos", serif;
                   font-weight: 700; font-size: 24px; color: var(--ink); }
  .section-lede { top: 522px; left: 140px; width: 608px; text-align: center; font-size: 11px; line-height: 18px; }

  .area-badge { width: 52px; height: 52px; border-radius: 50%; background: var(--white);
                box-shadow: 0 2px 9px var(--soft-shadow); display: flex; align-items: center; justify-content: center; }
  .area-label { font-size: 14px; color: var(--ink); white-space: nowrap; }

  .hub-name { left: 371px; top: 763px; width: 140px; text-align: center; font-family: "Tinos", serif; font-weight: 700;
              font-size: 17px; line-height: 20px; color: var(--gold); }

  .footer-art { position: absolute; left: 0; top: 1025px; width: 888px; height: 175px; }
  .contact-icon { width: 33px; height: 33px; border: 1px solid var(--gold); border-radius: 50%;
                  display: flex; align-items: center; justify-content: center; }
  .contact-head { font-family: "Tinos", serif; font-size: 11.5px; color: var(--white); }
  .contact-body { font-size: 9.5px; line-height: 14px; color: var(--white); }
  .footer-rule { left: 105px; top: 1155px; width: 678px; height: 1px; background: rgba(255,255,255,0.15); }
  .copyright { left: 0; top: 1172px; width: 888px; text-align: center; font-family: "Tinos", serif;
               font-size: 11px; color: var(--gold); }
</style>
</head>
<body>

<svg class="hero-art" viewBox="0 0 888 440" role="img" aria-label="Photograph looking up at glass office towers against a dusky sky">
  <defs>
    <linearGradient id="heroFill" x1="0" y1="0" x2="1" y2="1">
      <stop offset="0" stop-color="#4a4a4e"/>
      <stop offset="0.35" stop-color="#2c4a5a"/>
      <stop offset="0.7" stop-color="#1d5a70"/>
      <stop offset="1" stop-color="#0f3a4c"/>
    </linearGradient>
    <radialGradient id="heroGlow" cx="0.05" cy="0.2" r="0.5">
      <stop offset="0" stop-color="#8a7a45" stop-opacity="0.6"/>
      <stop offset="1" stop-color="#8a7a45" stop-opacity="0"/>
    </radialGradient>
  </defs>
  <path d="M0 0 H888 V368 Q444 470 0 368 Z" fill="url(#heroFill)"/>
  <path d="M0 0 H888 V368 Q444 470 0 368 Z" fill="url(#heroGlow)"/>
  <path d="M0 368 Q444 470 888 368" fill="none" stroke="var(--gold)" stroke-width="3"/>
</svg>

<div class="abs brand">
  <div class="brand-ring"></div>
  <div class="brand-name">R. T. HOLLOWAY, INC.</div>
</div>

<nav class="abs nav">
  <span>Home</span><span>About Us</span><span>Investment Areas</span><span>Social Responsibility</span>
</nav>
<div class="abs nav-cta">Contact Us</div>

<div class="abs hero-text hero-kicker">WELCOME TO R. T. HOLLOWAY, INC.</div>
<div class="abs hero-text hero-title">R. T. Holloway, Inc. Helps Develop Into A Great Nation And,<br>With Assertiveness, Stamp Its Footprint Worldwide</div>
<div class="abs hero-btn">Contact Us Today</div>

<h2 class="abs section-title">Our Investment Areas</h2>
<p class="abs section-lede">Lorem ipsum dolor sit amet, consectetuer adipiscing elit, sed diam nonummy nibh euismod tincidunt ut laoreet dolore magna aliquam erat volutpat. Ut wisi enim ad minim veniam, quis.</p>

<svg class="abs" style="left:0;top:0" width="888" height="1000" viewBox="0 0 888 1000" aria-hidden="true">
  <circle cx="441" cy="777" r="90" fill="none" stroke="var(--gold)" stroke-width="7"/>
  <g fill="var(--gold)" stroke="var(--white)" stroke-width="2">
    <circle cx="441" cy="688" r="5.5"/><circle cx="511" cy="719" r="5.5"/><circle cx="372" cy="719" r="5.5"/>
    <circle cx="360" cy="818" r="5.5"/><circle cx="521" cy="818" r="5.5"/><circle cx="441" cy="865" r="5.5"/>
  </g>
</svg>
<div class="abs hub-name">R. T. Holloway</div>

<!-- Real Estate -->
<div class="abs area-label" style="left:341px;top:582px;width:200px;text-align:center">Real Estate</div>
<div class="abs area-badge" style="left:415px;top:609px">
  <svg width="28" height="28" viewBox="0 0 28 28" fill="none" stroke-width="1.4"><path d="M6 13 L14 5 L22 13" stroke="var(--ink)"/><path d="M9 11 V18 H19 V11" stroke="var(--ink)"/><path d="M4 20 Q9 17 14 21 Q19 17 24 20 V24 H4 Z" stroke="var(--gold)"/></svg>
</div>

<!-- Healthcare -->
<div class="abs area-label" style="left:176px;top:703px;width:100px;text-align:right">Healthcare</div>
<div class="abs area-badge" style="left:291px;top:687px">
  <svg width="28" height="28" viewBox="0 0 28 28" fill="none" stroke-width="1.4"><path d="M14 17 L8 11 A3.5 3.5 0 0 1 14 6.5 A3.5 3.5 0 0 1 20 11 Z" stroke="var(--ink)"/><path d="M9 11 H12 L13 9 L15 13 L16 11 H19" stroke="var(--ink)"/><path d="M4 22 Q10 18 16 20 L22 18 Q24 19 22 21 L15 24 H4" stroke="var(--gold)"/></svg>
</div>

<!-- Energy -->
<div class="abs area-label" style="left:606px;top:704px">Energy</div>
<div class="abs area-badge" style="left:538px;top:687px">
  <svg width="28" height="28" viewBox="0 0 28 28" fill="none" stroke-width="1.4"><path d="M5 12 A9.5 9.5 0 0 1 22 9" stroke="var(--ink)"/><path d="M23 16 A9.5 9.5 0 0 1 6 19" stroke="var(--ink)"/><path d="M15 7 L11 15 H15 L13 21 L18 12 H14 Z" stroke="var(--gold)"/></svg>
</div>

<!-- Finance -->
<div class="abs area-label" style="left:174px;top:818px;width:100px;text-align:right">Finance</div>
<div class="abs area-badge" style="left:291px;top:800px">
  <svg width="28" height="28" viewBox="0 0 28 28" fill="none" stroke-width="1.4"><ellipse cx="19" cy="7" rx="5" ry="2" stroke="var(--ink)"/><path d="M14 7 V20 M24 7 V20 Q19 23 14 20 M14 11 Q19 14 24 11 M14 15.5 Q19 18.5 24 15.5" stroke="var(--ink)"/><circle cx="10" cy="17" r="6" stroke="var(--gold)" fill="var(--white)"/><path d="M11.5 14.5 H9.3 A1.2 1.2 0 0 0 9.3 17 H10.7 A1.2 1.2 0 0 1 10.7 19.5 H8.5 M10 13.5 V20.5" stroke="var(--gold)" stroke-width="1"/></svg>
</div>

<!-- Mining -->
<div class="abs area-label" style="left:605px;top:813px">Mining</div>
<div class="abs area-badge" style="left:538px;top:800px">
  <svg width="28" height="28" viewBox="0 0 28 28" fill="none" stroke-width="1.4"><circle cx="10" cy="11" r="5" stroke="var(--ink)"/><circle cx="10" cy="19" r="5" stroke="var(--ink)" fill="var(--white)"/><path d="M15 9 Q20 5 25 9" stroke="var(--gold)"/><path d="M20 7 V24" stroke="var(--gold)"/></svg>
</div>

<!-- Industry -->
<div class="abs area-badge" style="left:415px;top:886px">
  <svg width="30" height="30" viewBox="0 0 30 30" fill="none" stroke-width="1.4"><path d="M4 25 V15 L10 11 V15 L16 11 V15 L20 12 V4 H24 V25 Z" stroke="var(--ink)"/><path d="M8 19 V21 M12 19 V21 M16 19 V21" stroke="var(--gold)" stroke-width="1.8"/></svg>
</div>
<div class="abs area-label" style="left:341px;top:947px;width:206px;text-align:center">Industry</div>

<svg class="footer-art" viewBox="0 0 888 175" aria-hidden="true">
  <path d="M0 69 Q444 -50 888 69 V175 H0 Z" fill="var(--navy)"/>
  <path d="M0 69 Q444 -50 888 69" fill="none" stroke="var(--gold)" stroke-width="3"/>
</svg>

<div class="abs contact-icon" style="left:153px;top:1089px">
  <svg width="16" height="16" viewBox="0 0 16 16" fill="none" stroke="var(--gold)" stroke-width="1.1"><path d="M3 2 L6 2 L7 5 L5.5 6.5 Q7 9.5 9.5 10.5 L11 9 L14 10 V13 Q8 14 4.5 10 Q2 7 3 2 Z"/></svg>
</div>
<div class="abs contact-head" style="left:197px;top:1091px">Phone</div>
<div class="abs contact-body" style="left:197px;top:1106px">123-456-7890</div>

<div class="abs contact-icon" style="left:332px;top:1088px">
  <svg width="16" height="16" viewBox="0 0 16 16" fill="none" stroke="var(--gold)" stroke-width="1.1"><path d="M8 15 Q3 9 3 6 A5 5 0 0 1 13 6 Q13 9 8 15 Z"/><circle cx="8" cy="6" r="1.8"/></svg>
</div>
<div class="abs contact-head" style="left:378px;top:1087px">Address</div>
<div class="abs contact-body" style="left:378px;top:1104px">123 Lorem Ipsum Dolor Sit Amet,<br>Consectetuer Adipiscing.</div>

<div class="abs contact-icon" style="left:593px;top:1089px">
  <svg width="16" height="16" viewBox="0 0 16 16" fill="none" stroke="var(--gold)" stroke-width="1.1"><path d="M2 6 L8 2 L14 6 V14 H2 Z"/><path d="M2 6 L8 10 L14 6 M2 14 L6.5 9 M14 14 L9.5 9"/></svg>
</div>
<div class="abs contact-head" style="left:637px;top:1089px">Email</div>
<div class="abs contact-body" style="left:637px;top:1107px">info@rtholloway.com</div>

<div class="abs footer-rule"></div>
<div class="abs copyright">Copyright © 2021 R.T Holloway Inc.. All Rights Reserved.</div>

</body>
</html>
```